TAX SERVICES

I need a postcard design for a company 12 experience on Income tax preparation, base in 418 Linden Ridge Rd. Waterbury CT 06715 name "RV PELLON HARBOR LLC." This year we want to give 50 dollars discount for new customers
Industry/Entity Type
It Company

```html
<!DOCTYPE html>
<html lang="en">
<head>
<meta charset="utf-8">
<title>RV Pellon Harbor LLC – Income Tax Preparation Postcard</title>
<link rel="stylesheet" href="https://fonts.googleapis.com/css2?family=PT+Sans:wght@400;700&family=Oswald:wght@500;600&display=swap">
<style>
  :root {
    --navy: #17214a;
    --navy-deep: #111a3d;
    --gold: #f9c312;
    --band-yellow: #fccb0b;
    --white: #ffffff;
    --ink: #0d0f1a;
    --muted: #6b6e78;
    --photo-light: #e9ecf1;
    --photo-mid: #b9c0cb;
    --photo-dark: #4d5566;
  }
  * { margin: 0; padding: 0; box-sizing: border-box; }
  html, body {
    width: 1200px;
    height: 842px;
    overflow: hidden;
    background: var(--white);
  }
  .postcard {
    position: relative;
    width: 1200px;
    height: 842px;
    background: var(--navy);
    overflow: hidden;
    font-family: "PT Sans", Arial, sans-serif;
    color: var(--white);
  }
  .postcard__shapes {
    position: absolute;
    inset: 0;
  }
  .postcard__text {
    position: absolute;
    left: 44px;
    white-space: nowrap;
  }
  .company-name {
    top: 52px;
    font-size: 46px;
    font-weight: 700;
    letter-spacing: 0.5px;
  }
  .headline {
    top: 126px;
    font-size: 50px;
    font-weight: 400;
    color: var(--gold);
  }
  .tagline {
    top: 192px;
    font-size: 26px;
  }
  .services-title {
    top: 276px;
    font-size: 38px;
    color: var(--gold);
  }
  .services-list {
    top: 338px;
    list-style: none;
    font-size: 31px;
    line-height: 48.5px;
  }
  .services-list li::before {
    content: "» ";
    color: var(--gold);
  }
  .offer {
    top: 508px;
    left: 46px;
    display: flex;
    align-items: baseline;
    gap: 20px;
    font-family: "Oswald", "Arial Narrow", sans-serif;
    color: var(--ink);
  }
  .offer__amount {
    font-size: 104px;
    font-weight: 600;
    line-height: 1.1;
    letter-spacing: -1px;
  }
  .offer__label {
    font-size: 43px;
    font-weight: 500;
    letter-spacing: 0.3px;
  }
  .contact-intro {
    top: 726px;
    font-size: 23px;
    color: var(--muted);
  }
  .contact-line {
    top: 770px;
    display: flex;
    align-items: center;
    color: var(--ink);
  }
  .contact-line__phone {
    display: flex;
    align-items: center;
    gap: 12px;
    font-size: 40px;
    color: var(--navy-deep);
  }
  .contact-line__address {
    display: flex;
    align-items: center;
    gap: 12px;
    margin-left: 26px;
    font-size: 26px;
  }
  .icon { display: block; }
</style>
</head>
<body>
<main class="postcard">
  <svg class="postcard__shapes" width="1200" height="842" viewBox="0 0 1200 842" aria-hidden="false">
    <defs>
      <linearGradient id="photo-tones" x1="0" y1="0" x2="1" y2="1">
        <stop offset="0" stop-color="var(--photo-mid)"/>
        <stop offset="0.4" stop-color="var(--photo-light)"/>
        <stop offset="0.75" stop-color="var(--photo-mid)"/>
        <stop offset="1" stop-color="var(--photo-dark)"/>
      </linearGradient>
    </defs>
    <polygon class="photo-area" role="img"
      aria-label="Photo from above of two business people at a white round table working on a laptop and reviewing documents"
      points="620,0 1200,0 1200,842 1007,842" fill="url(#photo-tones)"/>
    <polygon class="accent-stripe" points="985,0 1040,0 830,300 812,272" fill="var(--navy)" opacity="0.85"/>
    <polygon class="offer-band" points="0,504 765,504 852,638 0,638" fill="var(--band-yellow)"/>
    <polygon class="contact-band" points="0,690 878,690 1007,842 0,842" fill="var(--white)"/>
  </svg>

  <h1 class="postcard__text company-name">RV PELLON HARBOR LLC.</h1>
  <h2 class="postcard__text headline">Income Tax Preparation</h2>
  <p class="postcard__text tagline">12 experience on Income tax preparation!</p>

  <h3 class="postcard__text services-title">SERVICES</h3>
  <ul class="postcard__text services-list">
    <li>Personal Tax Preparation</li>
    <li>Business Tax Preparation</li>
    <li>Health Insurance</li>
  </ul>

  <p class="postcard__text offer">
    <span class="offer__amount">50$</span>
    <span class="offer__label">DISCOUNT FOR NEW CUSTOMERS</span>
  </p>

  <p class="postcard__text contact-intro">Contact us today for a free, no obligation consultation:</p>
  <div class="postcard__text contact-line">
    <span class="contact-line__phone">
      <svg class="icon icon--phone" width="36" height="36" viewBox="0 0 24 24" aria-hidden="true">
        <path d="M6.6 10.8a15.2 15.2 0 0 0 6.6 6.6l2.2-2.2c.3-.3.7-.4 1-.2 1.1.4 2.3.6 3.6.6.6 0 1 .4 1 1V20c0 .6-.4 1-1 1A17 17 0 0 1 3 4c0-.6.4-1 1-1h3.5c.6 0 1 .4 1 1 0 1.3.2 2.5.6 3.6.1.3 0 .7-.2 1z" fill="var(--ink)"/>
        <path d="M14.5 2.5a7 7 0 0 1 7 7M14.5 5.5a4 4 0 0 1 4 4" stroke="#2f8fd8" stroke-width="1.6" fill="none" stroke-linecap="round"/>
      </svg>
      (203) 555-0148
    </span>
    <span class="contact-line__address">
      <svg class="icon icon--pin" width="24" height="32" viewBox="0 0 24 32" aria-hidden="true">
        <path d="M12 0a11 11 0 0 0-11 11c0 8 11 21 11 21s11-13 11-21A11 11 0 0 0 12 0zm0 15.5a4.5 4.5 0 1 1 0-9 4.5 4.5 0 0 1 0 9z" fill="var(--ink)"/>
      </svg>
      418 Linden Ridge Rd. Waterbury CT 06715
    </span>
  </div>
</main>
</body>
</html>
```